Velvet Root Studio- An All Natural Hair & Skincare Company needs a website design.

Velvet Root Studio is an all-natural Hair & Skin Company that provides all natural hair and skin care products to the ever growing natural hair community. Our primary target market is African American women between the ages of 16-50. I would like my website to be setup in a way that allows me to add photos, and products for sale easily. The site should be very user friendly but clean and professional looking. I have uploaded our new company Logo and I would definitely like it used throughout the pages. Ideally, the site should display our Motto, Company Vision, Pictures of Products and Results of use of products, testimonials from customers, Video tutorials. I need to be able to capture email addresses for easy email blasts and customer data collection, contact info, links to social media accounts, and detailed analytics to track traffic etc. I also need direct links to my CoinPouch and email.

It appears my brief is unclear. This is our first site. So i would like it to be able to showcase and all my products. I would like the coding for easy changes after the site goes live. I am not super tech savvy, but would like to be able to add new products and track traffic. Please let me know if this still needs clarification.

```html
<!DOCTYPE html>
<html lang="en">
<head>
<meta charset="utf-8">
<title>Velvet Root Studio — All Natural Hair &amp; Skin Care</title>
<link rel="stylesheet" href="https://fonts.googleapis.com/css2?family=Josefin+Sans:wght@300;400;600&family=Open+Sans:wght@400;600;700&family=Italianno&display=swap">
<style>
:root{
  --brown:#5e4b41;
  --brown-dark:#4a3a32;
  --orange:#f7941d;
  --ink:#333;
  --line:#555;
  --card-border:#e2e2e2;
  --price-bg:#eeeeee;
  --footer-bg:#f3f3f3;
  --quote-red:#c0392b;
  --band:#3a2f30;
}
*{box-sizing:border-box;margin:0;padding:0}
html,body{width:1200px;height:2305px;overflow:hidden;background:#fff}
body{position:relative;font-family:"Open Sans",Arial,sans-serif;color:var(--ink)}
a{color:inherit;text-decoration:none}

/* header */
.site-header{position:absolute;left:0;top:0;width:1200px;height:177px;background:#fff}
.brand{position:absolute;left:80px;top:20px;width:140px;text-align:center}
.brand-dot{width:84px;height:84px;border-radius:50%;background:var(--brown);margin:0 auto 12px}
.brand-name{font-family:"Josefin Sans",sans-serif;font-weight:400;font-size:16px;color:var(--brown);line-height:1.1;white-space:nowrap}
.search{position:absolute;left:783px;top:69px;width:182px;height:29px;border:1px solid #bbb;font-size:12px;color:#999;padding:6px 10px}
.search svg{position:absolute;right:9px;top:6px}
.cart{position:absolute;left:980px;top:70px;display:flex;align-items:center;gap:10px;font-size:11px;color:#777;font-weight:600}
.cart-icon{width:27px;height:27px;border-radius:50%;background:#c88d1c;display:flex;align-items:center;justify-content:center}
.user-links{position:absolute;left:622px;top:132px;display:flex;font-size:11px;font-weight:700;color:#222;letter-spacing:.3px;list-style:none}
.user-links .sep{margin:0 23px}

/* nav */
.main-nav{position:absolute;left:0;top:177px;width:1200px;height:49px;background:var(--brown)}
.main-nav ul{list-style:none}
.main-nav li{position:absolute;top:0;font-size:13px;font-weight:600;color:#fff;line-height:49px;letter-spacing:.2px;white-space:nowrap}
.main-nav li.active{background:var(--orange);width:100px;text-align:center}

/* hero */
.hero{position:absolute;left:0;top:226px;width:1200px;height:471px;background:linear-gradient(90deg,#d28a33,#e7a95a 50%,#d6913c)}
.hero-photo{position:absolute;left:0;top:0;width:705px;height:471px;background:linear-gradient(120deg,#f3f1f2 10%,#e7d6cf 45%,#f5efeb 80%);clip-path:polygon(0 0,702px 0,533px 471px,0 471px)}
.hero-edge{position:absolute;left:0;top:0}
.hero-brand{position:absolute;left:678px;top:90px;display:flex;align-items:center;gap:14px}
.hero-brand .brand-dot{width:66px;height:66px;margin:0;background:#4a3a32}
.hero-brand span{font-family:"Josefin Sans",sans-serif;font-size:16px;color:#fff;margin-top:30px}
.hero-title{position:absolute;left:671px;top:202px;font-family:"Josefin Sans",sans-serif;font-weight:400;font-size:41px;color:#3e2e25}
.hero-amp{position:absolute;left:982px;top:181px;font-family:"Josefin Sans",sans-serif;font-weight:300;font-size:110px;color:#fff;line-height:1}
.hero-sub{position:absolute;left:710px;top:246px;font-family:"Josefin Sans",sans-serif;font-size:33px;color:#fff}
.hero-tag{position:absolute;left:666px;top:295px;font-family:"Josefin Sans",sans-serif;font-weight:300;font-size:24px;color:#2e221c}
.shop-btn{position:absolute;left:671px;top:341px;width:205px;height:50px;display:flex;background:#8a6a55}
.shop-btn span{flex:1;color:#fff;font-family:"Josefin Sans",sans-serif;font-weight:300;font-size:26px;line-height:52px;padding-left:20px}
.shop-btn i{width:60px;background:var(--brown-dark);display:flex;align-items:center;justify-content:center}

/* section headings */
.section-title{position:absolute;font-family:"Josefin Sans",sans-serif;font-weight:300;font-size:28px;color:#222;white-space:nowrap}
.title-rule{position:absolute;height:2px;background:#888}
.title-rule::before{content:"";position:absolute;left:0;top:-2px;height:5px;width:126px;background:var(--line)}

/* products */
.product-card{position:absolute;top:818px;width:226px;height:238px;border:1px solid var(--card-border);background:#fff}
.product-shot{height:151px;background:radial-gradient(circle at 50% 55%,#f1e3c4,#fff 70%)}
.product-shot.soap{background:radial-gradient(circle at 50% 55%,#c9a57c,#fff 70%)}
.product-label{height:38px;background:var(--brown);color:#fff;font-family:"Josefin Sans",sans-serif;font-size:16px;line-height:40px;padding-left:19px;position:relative}
.product-label::after{content:"";position:absolute;right:12px;top:9px;width:20px;height:20px;border-radius:50%;background:#e9dfd6}
.product-buy{display:flex;height:47px;background:var(--price-bg)}
.price{width:114px;font-size:14px;font-weight:700;line-height:47px;text-align:center;color:#222;border-right:1px solid #d8d8d8}
.add-cart{flex:1;font-size:12px;line-height:47px;text-align:center;color:#333}

/* video */
.video-frame{position:absolute;left:120px;top:1140px;width:396px;height:262px;background:#b5b5b5;border-radius:6px;box-shadow:0 16px 14px -8px rgba(0,0,0,.35)}
.video-still{position:absolute;left:11px;top:9px;width:376px;height:243px;background:linear-gradient(135deg,#f4e5ea,#f9f2f3 55%,#ead6dc)}
.video-play{position:absolute;left:176px;top:103px}
.video-copy{position:absolute;left:565px;top:1176px;width:510px;font-family:Arial,sans-serif;font-size:13.5px;line-height:20px;color:#222;text-align:justify}
.video-copy p+p{margin-top:20px}
.quote-mark{position:absolute;left:571px;top:1322px;font-family:Georgia,serif;font-size:60px;color:var(--quote-red);line-height:1;font-style:italic}
.promo{position:absolute;left:611px;top:1343px;font-family:"Italianno",cursive;font-size:38px;line-height:29px;color:#777;white-space:nowrap}
.promo span{display:block;padding-left:83px}

/* testimonials */
.testimonials{position:absolute;left:0;top:1482px;width:1200px;height:440px;background:linear-gradient(180deg,#453a3b,#332a2c 60%,#3d2f2e)}
.testimonials .section-title{color:#fff}
.testimonials .title-rule{background:#cfcfcf}
.testimonials .title-rule::before{background:#fff}
.quote-box{position:absolute;top:131px;width:283px;height:125px;border:2px solid #fff;padding:12px 8px 0 24px;font-family:Arial,sans-serif;font-size:12px;font-weight:700;color:#fff;line-height:18px}
.quote-box::before,.quote-box::after{content:"";position:absolute;left:212px;width:0;height:0;border-style:solid}
.quote-box::before{bottom:-14px;border-width:14px 0 0 16px;border-color:#fff transparent transparent transparent}
.quote-box::after{bottom:-10px;left:214px;border-width:10px 0 0 11px;border-color:var(--band) transparent transparent transparent}
.author{position:absolute;top:273px;display:flex;align-items:center;gap:16px}
.author-photo{width:60px;height:60px;border-radius:50%;border:3px solid var(--orange);background:linear-gradient(135deg,#f3dede,#c9a1a0)}
.author-name{font-family:Arial,sans-serif;font-size:13px;font-weight:700;color:var(--orange);line-height:18px}
.author-name b{display:block;color:#fff}

/* footer */
.site-footer{position:absolute;left:0;top:1922px;width:1200px;height:290px;background:var(--footer-bg)}
.footer-brand{position:absolute;left:88px;top:42px;width:140px;text-align:center}
.footer-brand .brand-dot{width:84px;height:84px}
.payments{position:absolute;left:108px;top:208px;display:flex;gap:10px;font-size:12px;font-weight:700;color:#2a4a8c}
.footer-col{position:absolute;top:49px}
.footer-col h4{font-size:15px;font-weight:400;color:#222;margin-bottom:12px}
.footer-col ul{list-style:none}
.footer-col li{font-size:13px;color:#444;line-height:24px}
.footer-divider{position:absolute;top:44px;height:212px;border-left:1px dotted #999}
.socials{display:flex;gap:9px;margin-top:10px}
.socials span{width:22px;height:22px;background:#3b5998;color:#fff;font-size:7px;line-height:22px;text-align:center;overflow:hidden}
.socials span:nth-child(2){background:#2aa9e0}
.socials span:nth-child(3){background:#444}
.map{position:absolute;left:793px;top:84px;width:299px;height:134px;border:4px solid #ccc;background:linear-gradient(135deg,#e8e5dc,#f2efe7)}
.copyright{position:absolute;left:0;top:2212px;width:1200px;height:93px;background:#fff;text-align:center;font-family:Arial,sans-serif;font-size:13px;color:#555;line-height:76px}
</style>
</head>
<body>

<header class="site-header">
  <div class="brand"><div class="brand-dot"></div><div class="brand-name">Velvet Root Studio</div></div>
  <div class="search">Search ...
    <svg width="16" height="16" viewBox="0 0 16 16"><circle cx="6" cy="6" r="4.5" fill="none" stroke="#222" stroke-width="2"/><line x1="9.5" y1="9.5" x2="14" y2="14" stroke="#222" stroke-width="2.4"/></svg>
  </div>
  <div class="cart"><span class="cart-icon"><svg width="14" height="12" viewBox="0 0 14 12"><path d="M0 1h3l2 7h7l2-5H4" fill="none" stroke="#fff" stroke-width="1.6"/><circle cx="6" cy="10.5" r="1.2" fill="#fff"/><circle cx="11" cy="10.5" r="1.2" fill="#fff"/></svg></span>CART (0)</div>
  <ul class="user-links">
    <li>ACCOUNT</li><li class="sep">|</li><li>WISHLIST</li><li class="sep">|</li><li>CHECKOUT</li><li class="sep">|</li><li>LOGIN</li><li class="sep">|</li><li>SIGNUP</li>
  </ul>
</header>

<nav class="main-nav">
  <ul>
    <li class="active" style="left:100px">HOME</li>
    <li style="left:224px">CATEGORIES</li>
    <li style="left:361px">FAQ'S</li>
    <li style="left:449px">GALLERY</li>
    <li style="left:555px">SHOPPING CART</li>
    <li style="left:710px">OUR PARTNERS</li>
    <li style="left:861px">CONTACT US</li>
    <li style="left:991px">SITEMAP</li>
  </ul>
</nav>

<section class="hero">
  <div class="hero-photo" role="img" aria-label="Portrait of a woman with long flowing auburn curls"></div>
  <svg class="hero-edge" width="1200" height="471"><line x1="702" y1="0" x2="533" y2="471" stroke="#fff" stroke-width="4"/></svg>
  <div class="hero-brand"><div class="brand-dot"></div><span>Velvet Root Studio</span></div>
  <div class="hero-title">All Natural hair</div>
  <div class="hero-amp">&amp;</div>
  <div class="hero-sub">Skin Care Products</div>
  <div class="hero-tag">ever growing natural hair community</div>
  <a class="shop-btn"><span>Shop Now</span><i><svg width="10" height="14" viewBox="0 0 10 14"><path d="M2 2l5 5-5 5" fill="none" stroke="#f7941d" stroke-width="2.4"/></svg></i></a>
</section>

<h2 class="section-title" style="left:114px;top:743px">Our Products</h2>
<div class="title-rule" style="left:286px;top:762px;width:797px"></div>

<div class="product-card" style="left:114px"><div class="product-shot" role="img" aria-label="Bottles of natural hair lotion"></div><div class="product-label">Mauris Eleifend</div><div class="product-buy"><div class="price">1140,00 €</div><div class="add-cart">+ Add to Cart</div></div></div>
<div class="product-card" style="left:362px"><div class="product-shot soap" role="img" aria-label="Natural soap bars and balm tins"></div><div class="product-label">Curabitur Sit Amet</div><div class="product-buy"><div class="price">2850,00 €</div><div class="add-cart">+ Add to Cart</div></div></div>
<div class="product-card" style="left:610px"><div class="product-shot" role="img" aria-label="Bottles of natural hair lotion"></div><div class="product-label">Etiam Ultricies</div><div class="product-buy"><div class="price">1254,00 €</div><div class="add-cart">+ Add to Cart</div></div></div>
<div class="product-card" style="left:858px"><div class="product-shot soap" role="img" aria-label="Natural soap bars and balm tins"></div><div class="product-label">Adipiscing Sem</div><div class="product-buy"><div class="price">3990,00 €</div><div class="add-cart">+ Add to Cart</div></div></div>

<div class="video-frame">
  <div class="video-still" role="img" aria-label="Video tutorial still of a smiling woman"></div>
  <svg class="video-play" width="60" height="60" viewBox="0 0 60 60"><circle cx="30" cy="30" r="27" fill="#fff" stroke="#444" stroke-width="4"/><path d="M23 17l18 13-18 13z" fill="#333"/></svg>
</div>
<h2 class="section-title" style="left:558px;top:1138px">Our Vedio Tutorial</h2>
<div class="title-rule" style="left:791px;top:1156px;width:284px"></div>
<div class="video-copy">
  <p>Lorem Ipsum is simply dummy text of the printing and typesetting industry. Lorem Ipsum has been the industry's standard dummy text ever since the 1500s, when an unknown printer took a galley of type and scrambled It has survived not only five centuries, but also the leap into electronic typesetting,</p>
  <p>It was popularised in the 1960s with the release of Typeline sheets containing Lorem Ipsum passages, and more recently with desktop.</p>
</div>
<div class="quote-mark">“</div>
<div class="promo">Your promotional text here Vivamus<span>volutpat ante, sit amet semper nisi</span></div>

<section class="testimonials">
  <h2 class="section-title" style="left:118px;top:46px">Our Products</h2>
  <div class="title-rule" style="left:292px;top:63px;width:796px"></div>

  <div class="quote-box" style="left:140px">Lorem ipsum dolor sit amet, consectetur adipisicing elit, sed do eiusmod tempor incididunt ut labore et dolore magna aliqua. Ut enim ad minim veniam, quis nostrud exercitation ullamco laboris</div>
  <div class="author" style="left:173px"><div class="author-photo" role="img" aria-label="Customer portrait"></div><div class="author-name">Dana Miles, COO,<b>Lumen Co</b></div></div>

  <div class="quote-box" style="left:466px">Lorem ipsum dolor sit amet, consectetur adipisicing elit, sed do eiusmod tempor incididunt ut labore et dolore magna aliqua. Ut enim ad minim veniam, quis nostrud exercitation ullamco laboris</div>
  <div class="author" style="left:499px"><div class="author-photo" role="img" aria-label="Customer portrait"></div><div class="author-name">Dana Miles, COO,<b>Lumen Co</b></div></div>

  <div class="quote-box" style="left:793px">Lorem ipsum dolor sit amet, consectetur adipisicing elit, sed do eiusmod tempor incididunt ut labore et dolore magna aliqua. Ut enim ad minim veniam, quis nostrud exercitation ullamco laboris</div>
  <div class="author" style="left:826px"><div class="author-photo" role="img" aria-label="Customer portrait"></div><div class="author-name">Dana Miles, COO,<b>Lumen Co</b></div></div>
</section>

<footer class="site-footer">
  <div class="footer-brand"><div class="brand-dot"></div><div class="brand-name">Velvet Root Studio</div></div>
  <div class="payments"><span>Paxa</span><span>DuoCard</span><span>Vantage</span><span>CoinPouch</span></div>

  <div class="footer-col" style="left:284px"><h4>Support Links</h4><ul><li>Terms and conditions</li><li>Legal Notice</li><li>Private Policy</li></ul></div>
  <div class="footer-divider" style="left:470px"></div>
  <div class="footer-col" style="left:524px"><h4>Contact Info</h4><ul><li>42 Willow Crest Avenue</li><li>Suite 210</li><li>Fairhaven, FL 30000</li><li>Phone: 555 010-2288</li><li>Fax: 555 010-2299</li></ul>
    <div class="socials"><span>Folio</span><span>Chirp</span><span>Circ</span></div></div>
  <div class="footer-divider" style="left:760px"></div>
  <div class="footer-col" style="left:793px"><h4>Find Us</h4></div>
  <div class="map" role="img" aria-label="Street map showing the studio location"></div>
</footer>

<div class="copyright">Copyright 2015 velvet root studio. All Rights Reserved</div>

</body>
</html>
```